Clean professional design needed for landscape property business

We need a logo for a new lawncare, landscaping , property maintenance business called Meadow Trim.
Our services include lawn mowing, garden maintenance, clean ups and some property maintenance.
We want a double sided business card that is clean and very professional using the colour scheme from our logo which is provided.
the business card should have impact as we will use these to drop into people's letterboxes as a marketing drop.
Initially we want to see what you come up with so there is a very wide scope here to work with.
Updates

Project Deadline Extended
Reason: we feel our original deadline was too short. we have extended to give more time for quality submissions.

Target Market(s)

High end property owners who don't wish to do there own gardneing or property maintenance

Industry/Entity Type

Business

Contact Information for Business Card

Name
Postion/ Title
Phone number
mobile
web address
physical address

services offered

Font styles to use
Sans Serif

Requirements
Must have
• curved edges preferrred
Nice to have
• We like the idea of the logo being embossed or etched into the card so it looks like it is below the surface of the card
Should not have
• No stock images or characters.

```html
<!DOCTYPE html>
<html lang="en">
<head>
<meta charset="utf-8">
<title>Meadow Trim – Business Card</title>
<link href="https://fonts.googleapis.com/css2?family=Montserrat:wght@600;700&family=Questrial&display=swap" rel="stylesheet">
<style>
  :root {
    --bg: #2b2c2e;
    --green: #7cc242;
    --green-light: #97d352;
    --white: #ffffff;
    --paper: #f7f7f7;
    --grey: #5b5c5e;
    --rule: #b9b9b9;
  }
  * { box-sizing: border-box; margin: 0; padding: 0; }
  html, body { width: 1200px; height: 900px; overflow: hidden; }
  body { background: var(--bg); position: relative; font-family: "Questrial", sans-serif; }

  .card {
    position: absolute;
    width: 560px;
    height: 320px;
    border-radius: 26px;
    overflow: hidden;
  }
  .card-front {
    left: 70px; top: 80px;
    background: radial-gradient(circle at 45% 35%, var(--green-light), var(--green) 75%);
  }
  .card-back {
    left: 570px; top: 490px;
    background: linear-gradient(160deg, var(--white), var(--paper));
  }

  .grass-band { position: absolute; left: 0; bottom: 0; width: 100%; height: 62px; display: block; }

  .front-brand {
    position: absolute; left: 0; right: 0; top: 96px;
    text-align: center;
    font-family: "Montserrat", sans-serif; font-weight: 700;
    font-size: 56px; letter-spacing: -2px; color: var(--white);
  }
  .front-web {
    position: absolute; left: 0; right: 0; top: 186px;
    text-align: center;
    font-family: "Montserrat", sans-serif; font-weight: 600;
    font-size: 14px; letter-spacing: 2px; color: var(--white);
  }

  .back-brand {
    position: absolute; left: 30px; top: 62px;
    display: flex; align-items: center; gap: 12px;
    font-family: "Montserrat", sans-serif; font-weight: 700;
    font-size: 40px; line-height: 50px; letter-spacing: -1.5px; color: var(--green);
    white-space: nowrap;
  }
  .brand-square { width: 18px; height: 18px; background: var(--grey); }

  .person {
    position: absolute; left: 40px; width: 244px; top: 156px;
    text-align: right;
  }
  .person-title { font-size: 17px; line-height: 22px; color: var(--grey); }
  .person-name {
    font-family: "Montserrat", sans-serif; font-weight: 700;
    font-size: 18px; line-height: 24px; color: var(--green); letter-spacing: 0.5px;
  }
  .divider {
    position: absolute; left: 300px; top: 134px;
    width: 1px; height: 106px; background: var(--rule);
  }
  .contacts {
    position: absolute; left: 316px; top: 130px;
    list-style: none; font-size: 15px; color: var(--grey); line-height: 22px;
    white-space: nowrap;
  }
  .contacts li { display: flex; align-items: flex-start; gap: 8px; }
  .contacts svg { width: 13px; height: 13px; margin-top: 4px; flex: none; fill: var(--green); }
  .contacts .gap { margin-top: 4px; }
</style>
</head>
<body>

  <section class="card card-front" aria-label="Card front">
    <div class="front-brand">meadowtrim</div>
    <div class="front-web">www.meadowtrim.com</div>
    <svg class="grass-band" viewBox="0 0 560 62" preserveAspectRatio="none" role="img" aria-label="Grass silhouette edge along the bottom of the card">
      <rect x="0" y="14" width="560" height="48" fill="#ffffff"/>
    </svg>
  </section>

  <section class="card card-back" aria-label="Card back">
    <div class="back-brand">meadowtrim <span class="brand-square"></span></div>

    <div class="person">
      <div class="person-title">Director</div>
      <div class="person-name">OWEN HARTLEY</div>
    </div>

    <div class="divider"></div>

    <ul class="contacts">
      <li><svg viewBox="0 0 12 12"><rect x="3" y="0.5" width="6" height="11" rx="1.2" fill="none" stroke="#7cc242" stroke-width="1.2"/></svg>0412 306 718</li>
      <li><svg viewBox="0 0 12 12"><path d="M1 4c0-2 2-3 5-3s5 1 5 3l-2 1-1-1.5H4L3 5zM3 6h6l1.5 5h-9z"/></svg>(02) 4631 0927</li>
      <li><svg viewBox="0 0 12 12"><circle cx="6" cy="6" r="5.2" fill="none" stroke="#7cc242" stroke-width="1.2"/><path d="M1 6h10M6 1c-2 2.5-2 7.5 0 10M6 1c2 2.5 2 7.5 0 10" fill="none" stroke="#7cc242" stroke-width="1"/></svg>www.meadowtrim.com</li>
      <li class="gap"><svg viewBox="0 0 12 12"><path d="M6 0.5a4 4 0 0 1 4 4c0 3-4 7-4 7s-4-4-4-7a4 4 0 0 1 4-4z"/><circle cx="6" cy="4.5" r="1.5" fill="#ffffff"/></svg><span>14 Willow Lane, Elmsford<br>P.O Box 2210 Greenvale</span></li>
    </ul>

    <svg class="grass-band" viewBox="0 0 560 62" preserveAspectRatio="none" role="img" aria-label="Green grass silhouette edge along the bottom of the card">
      <defs>
        <linearGradient id="grassFill" x1="0" y1="0" x2="0" y2="1">
          <stop offset="0" stop-color="#8fcf4c"/>
          <stop offset="1" stop-color="#7cc242"/>
        </linearGradient>
      </defs>
      <rect x="0" y="14" width="560" height="48" fill="url(#grassFill)"/>
    </svg>
  </section>

</body>
</html>
```